Easter. Company for collection, treatment and recovery of dangerous and dangerous goods. not dangerous

We need an image folder with 4 pages, details see insert, logo can not be changed and some pictures collection and treatment of hazardous and non-hazardous waste, Tankwageninnenreinigung own fleet

Target Market(s)

existing customers and new customers

Colors

Designer to choose colors to be used in the design.

Requirements
Must have
• BRAV logo
Nice to have
• Design the text and the pictures so that it suits our disposal company. You can also use the pictures from our webside.

```html
<!DOCTYPE html>
<html lang="de">
<head>
<meta charset="utf-8">
<title>BRAV – Mappe und Einleger</title>
<link href="https://fonts.googleapis.com/css2?family=Lato:wght@400;700;900&display=swap" rel="stylesheet">
<style>
  :root{
    --green:#1f6b3d;
    --green-dark:#134a2a;
    --green-light:#3d9a55;
    --ink:#222;
    --muted:#555;
    --paper:#fff;
    --stage:#e4e4e4;
    --black:#161616;
  }
  *{box-sizing:border-box;margin:0;padding:0}
  html,body{width:960px;height:1200px;overflow:hidden}
  body{background:var(--stage);font-family:'Lato',sans-serif;color:var(--ink);position:relative}
  .page{position:absolute;width:300px;height:424px;background:var(--paper);overflow:hidden;box-shadow:0 3px 10px rgba(0,0,0,.18)}
  .page svg.art{position:absolute;inset:0;width:300px;height:424px}
  .abs{position:absolute}
  .brand{font-weight:900;color:var(--green);letter-spacing:1px;display:flex;align-items:center;gap:5px}
  .brand .dot{width:9px;height:9px;border-radius:50%;background:var(--green)}
  .brand.light{color:#fff}
  .brand.light .dot{background:#fff}
  .small{font-size:4.6px;line-height:1.45;color:var(--muted)}
  .small ul{list-style:none}
  .small li::before{content:"• ";color:var(--green)}
  .sub{font-size:5.2px;font-weight:700;color:var(--ink);margin:3px 0 1px}
  .title{font-size:11px;color:var(--ink);font-weight:400}
  .title b{color:var(--green);font-weight:700}
  .title .caps{font-size:9.5px}
  .h-green{font-size:10px;font-weight:700;color:var(--green);letter-spacing:.2px}
  .hotline{display:flex;align-items:center;gap:8px}
  .hotline .ic{width:18px;height:18px;border-radius:50%;border:2px solid var(--green);display:flex;align-items:center;justify-content:center}
  .hotline strong{display:block;font-size:8px}
  .hotline span{font-size:6.5px}
  .contact{font-size:5.6px;line-height:2.1}
  .contact i{display:inline-block;width:5px;height:5px;background:var(--green);border-radius:1px;margin-right:10px;vertical-align:middle}
  .services{font-size:5px;color:var(--ink);column-count:2;column-gap:14px;line-height:1.6}
  .services div::before{content:"• ";color:var(--green)}
  .badge{width:14px;height:14px;border-radius:50%;display:inline-block;margin-right:5px}
</style>
</head>
<body>

<!-- Outer spread: back cover -->
<section class="page back-cover" style="left:15px;top:150px">
  <svg class="art" viewBox="0 0 300 424">
    <defs>
      <linearGradient id="plant" x1="0" y1="0" x2="1" y2="1"><stop offset="0" stop-color="#7d93a8"/><stop offset="1" stop-color="#4a5a66"/></linearGradient>
    </defs>
    <path d="M0 0H150Q175 60 130 110Q80 150 0 150Z" fill="var(--green)"/>
    <path d="M0 0H140Q160 58 120 100Q75 138 0 140Z" fill="url(#plant)" role="img" aria-label="Luftbild des Firmenstandorts mit Hallen und Fahrzeugen"/>
    <path d="M0 330Q150 350 300 335V424H0Z" fill="#f1f1f1"/>
  </svg>
  <p class="abs small" style="left:18px;top:160px;width:180px">Die BRAV Umweltschutz und Wertstoff-Recycling GmbH ist ein modernes, mittelständisches Dienstleistungsunternehmen im Zentralraum, welches mit jeweils dem Stand der Technik entsprechenden Verfahren eine Vielzahl von Lösungen im Bereich der Entsorgung und Recyclingwirtschaft anbietet. BRAV ist seit 1976 am Standort Lindenau, Industriestraße 12, tätig.</p>
  <div class="abs" style="left:18px;top:212px">
    <span class="badge" style="background:#5b7fa3"></span><span class="badge" style="background:#e0a23a"></span><span class="badge" style="background:#e07d2c"></span><span class="badge" style="background:#4f8fc9"></span>
  </div>
  <div class="abs brand" style="left:18px;top:240px;font-size:17px"><span class="dot"></span>BRAV</div>
  <div class="abs hotline" style="left:150px;top:286px">
    <div class="ic"><svg width="9" height="9" viewBox="0 0 24 24"><path d="M6 2l4 4-2 3c1 2 4 5 6 6l3-2 4 4-3 4C10 21 3 14 2 5z" fill="var(--green)"/></svg></div>
    <div><strong>24h Notdienst:</strong><span>0699/00 12 34 56</span></div>
  </div>
  <div class="abs contact" style="left:18px;top:338px">
    <div><i></i>43 (0) 7000 / 12 34 5</div>
    <div><i></i>43 (0) 7000 / 12 34 6</div>
    <div><i></i>www.brav.at</div>
    <div><i></i>office@brav.at</div>
    <div><i></i>tankcleaning@brav.at</div>
  </div>
</section>

<!-- Outer spread: front cover -->
<section class="page front-cover" style="left:315px;top:150px">
  <svg class="art" viewBox="0 0 300 424">
    <defs>
      <linearGradient id="field" x1="0" y1="0" x2="0" y2="1"><stop offset="0" stop-color="#6fa67a"/><stop offset=".5" stop-color="#2f7a40"/><stop offset="1" stop-color="#154a24"/></linearGradient>
    </defs>
    <path d="M0 160Q20 290 170 290Q250 288 300 262V275Q240 305 165 305Q10 300 0 175Z" fill="var(--green)"/>
    <path d="M0 0H300V255Q240 282 170 282Q25 280 0 150Z" fill="url(#field)" role="img" aria-label="Grüne Reisterrassen im Morgenlicht"/>
    <path d="M0 175Q14 312 165 315Q240 315 300 285V290Q240 322 165 322Q8 318 0 185Z" fill="var(--green-light)"/>
  </svg>
  <div class="abs brand" style="left:22px;top:330px;font-size:19px"><span class="dot"></span>BRAV</div>
  <div class="abs services" style="left:140px;top:328px;width:150px">
    <div>Abfallsammlung</div><div>Abfallentsorgung</div><div>Reinigung von Industrieanlagen und Behältern</div><div>Abfallbehandlung</div><div>Tankwageninnen&shy;reinigung</div>
  </div>
</section>

<!-- Inside: left flap -->
<section class="page inside-flap" style="left:645px;top:150px;background:var(--green)">
  <svg class="art" viewBox="0 0 300 424"><rect y="404" width="300" height="20" fill="var(--black)"/></svg>
  <div class="abs brand light" style="left:80px;top:120px;font-size:26px"><span class="dot"></span>BRAV</div>
</section>

<!-- Inside: right page with pocket -->
<section class="page inside-pocket" style="left:15px;top:626px">
  <svg class="art" viewBox="0 0 300 424">
    <defs>
      <linearGradient id="hall" x1="0" y1="0" x2="1" y2="1"><stop offset="0" stop-color="#c9b04a"/><stop offset="1" stop-color="#3d5a2a"/></linearGradient>
      <linearGradient id="pocket" x1="0" y1="0" x2="0" y2="1"><stop offset="0" stop-color="#fafafa"/><stop offset="1" stop-color="#e6e6e6"/></linearGradient>
    </defs>
    <circle cx="205" cy="360" r="62" fill="var(--green)"/>
    <circle cx="205" cy="360" r="56" fill="url(#hall)" role="img" aria-label="Innenansicht der Reinigungsanlage mit Rohrleitungen"/>
    <path d="M0 300Q110 265 170 300Q200 320 230 330L300 330V424H0Z" fill="url(#pocket)" stroke="#d5d5d5"/>
    <rect y="404" width="40" height="20" fill="var(--black)"/>
  </svg>
  <p class="abs title" style="left:18px;top:20px">Unsere <b>Dienstleistungen</b> <span class="caps">UND <b>SCHWERPUNKTE</b></span></p>
  <div class="abs small" style="left:18px;top:44px;width:130px">
    <div class="sub">Entsorgungsdienstleistungen</div>
    <ul><li>Sammlung, Behandlung, Verwertung</li><li>Entleerung und Reinigung von Gruben</li><li>Reinigung von Industrieanlagen</li><li>Sanierung von Altlasten</li></ul>
  </div>
  <div class="abs small" style="left:160px;top:44px;width:125px">
    <div class="sub">Standorte und Kompetenzen</div>
    <ul><li>Standort mit Lager und Anlage</li><li>Tankwagenreinigung mit 4 Bahnen</li><li>Eigener Fuhrpark</li></ul>
  </div>
  <p class="abs h-green" style="left:18px;top:112px">TANKWAGENREINIGUNG</p>
  <p class="abs small" style="left:18px;top:128px;width:265px">Einer der ersten Tankwageninnenreinigungsanlagen des Landes, seit 1995 am Standort in Lindenau. Reinigung einer umfangreichen Produktpalette inklusive spezieller Problemprodukte.</p>
  <div class="abs hotline" style="left:18px;top:165px">
    <div class="ic"><svg width="9" height="9" viewBox="0 0 24 24"><path d="M6 2l4 4-2 3c1 2 4 5 6 6l3-2 4 4-3 4C10 21 3 14 2 5z" fill="var(--green)"/></svg></div>
    <div><strong>24h Notdienst:</strong><span>0699/00 12 34 56</span></div>
  </div>
  <div class="abs contact" style="left:18px;top:192px"><div><i></i>www.brav.at</div><div><i></i>tankcleaning@brav.at</div></div>
  <div class="abs brand" style="left:180px;top:250px;font-size:15px"><span class="dot"></span>BRAV</div>
</section>

<!-- Insert 1 -->
<section class="page insert-services" style="left:330px;top:626px">
  <svg class="art" viewBox="0 0 300 424">
    <defs>
      <linearGradient id="fade1" x1="0" y1="0" x2="0" y2="1"><stop offset="0" stop-color="#fff"/><stop offset="1" stop-color="#e9e9e9"/></linearGradient>
      <linearGradient id="hall2" x1="0" y1="0" x2="1" y2="1"><stop offset="0" stop-color="#d4c258"/><stop offset="1" stop-color="#2f5a2c"/></linearGradient>
    </defs>
    <rect y="250" width="300" height="174" fill="url(#fade1)"/>
    <circle cx="248" cy="340" r="70" fill="var(--green)"/>
    <circle cx="248" cy="340" r="63" fill="url(#hall2)" role="img" aria-label="Reinigungsanlage mit Rohrleitungen und Schaltschränken"/>
    <path d="M0 374Q150 370 300 350V362Q150 382 0 386Z" fill="var(--green)"/>
    <path d="M0 386Q150 382 300 362V424H0Z" fill="var(--black)"/>
  </svg>
  <p class="abs title" style="left:18px;top:18px">Unsere <b>Dienstleistungen</b> <span class="caps">UND <b>SCHWERPUNKTE</b></span></p>
  <div class="abs small" style="left:20px;top:38px;width:130px">
    <div class="sub">Entsorgungsdienstleistungen und Abfallmanagement</div>
    <ul><li>Sammlung, Behandlung, Verwertung von Abfällen</li><li>gefährlicher und nicht gefährlicher Art</li><li>in flüssiger, fester und pastöser Form</li></ul>
    <ul style="margin-top:3px"><li>Entleerung und Reinigung von:</li><li>Rohr-, Kanal- und Tankanlagen</li><li>Gruben und Sickerschächten</li><li>Öl- und Fettabscheidern</li></ul>
    <ul style="margin-top:3px"><li>Reinigung von Industrieanlagen</li><li>Abwasser- und Abfallanalytik</li><li>TV-Kanalinspektion</li><li>Sanierung von Altlasten</li><li>Behälter- und Containerservice</li></ul>
  </div>
  <div class="abs small" style="left:160px;top:38px;width:125px">
    <div class="sub">Tankwageninnenreinigung</div>
    <ul><li>Lebensmittel Produkte</li><li>Chemische Produkte</li><li>Alle Klassen außer 1, 2, 7</li><li>Reinigung von Fässern und Behältern</li></ul>
    <div class="sub">Standorte, Anlagen und Kompetenzen</div>
    <ul><li>Standorte im Zentralraum</li><li>Chemisch-physikalisch-biologische Anlage zur Behandlung von Abfällen</li><li>Tankwagenreinigungsanlage mit 4 Bahnen</li><li>Fuhrpark zur Sammlung und Transport (Tochterfirma NORDA)</li><li>Umfangreicher Genehmigungskatalog</li></ul>
  </div>
  <p class="abs h-green" style="left:24px;top:160px">TANKWAGENREINIGUNG</p>
  <p class="abs small" style="left:24px;top:176px;width:250px">Einer der ersten Tankwageninnenreinigungsanlagen des Landes, seit 1995 am Standort in Lindenau, Industriestraße 12. Mit 4 Reinigungsbahnen, 15 Waschköpfen, Dampf, Trocknungsanlage, Verpflegung und Dusche für die Fahrer.</p>
  <p class="abs small" style="left:24px;top:200px;width:250px">Die Anlage arbeitet nach den Bestimmungen der europäischen Branchenverbände und ist auditiert. Die erfolgte Reinigung bestätigen wir Ihnen mit einem Reinigungsdokument.</p>
  <div class="abs hotline" style="left:24px;top:228px">
    <div class="ic"><svg width="9" height="9" viewBox="0 0 24 24"><path d="M6 2l4 4-2 3c1 2 4 5 6 6l3-2 4 4-3 4C10 21 3 14 2 5z" fill="var(--green)"/></svg></div>
    <div><strong>24h Notdienst:</strong><span>0699/00 12 34 56</span></div>
  </div>
  <div class="abs contact" style="left:24px;top:252px"><div><i></i>www.brav.at</div><div><i></i>tankcleaning@brav.at</div></div>
  <div class="abs brand" style="left:192px;top:240px;font-size:15px"><span class="dot"></span>BRAV</div>
</section>

<!-- Insert 2 -->
<section class="page insert-plant" style="left:645px;top:626px">
  <svg class="art" viewBox="0 0 300 424">
    <defs>
      <linearGradient id="fade2" x1="0" y1="0" x2="0" y2="1"><stop offset="0" stop-color="#fff"/><stop offset="1" stop-color="#e6e6e6"/></linearGradient>
      <linearGradient id="truck" x1="0" y1="0" x2="1" y2="1"><stop offset="0" stop-color="#4a8fd6"/><stop offset=".7" stop-color="#1f5fa8"/><stop offset="1" stop-color="#2a2a2a"/></linearGradient>
    </defs>
    <rect y="230" width="300" height="194" fill="url(#fade2)"/>
    <circle cx="250" cy="340" r="76" fill="var(--green)"/>
    <circle cx="250" cy="340" r="69" fill="url(#truck)" role="img" aria-label="Blauer Saugwagen des Fuhrparks"/>
    <path d="M0 374Q150 370 300 350V362Q150 382 0 386Z" fill="var(--green)"/>
    <path d="M0 386Q150 382 300 362V424H0Z" fill="var(--black)"/>
  </svg>
  <p class="abs title" style="left:18px;top:20px;font-size:10px">CPB – CHEMISCH-PHYSIKALISCH-<br><b style="font-size:11px">BIOLOGISCHE-ANLAGE</b></p>
  <p class="abs small" style="left:18px;top:50px;width:265px">Unsere CPB-Anlage stellt landesweit einen einzigartigen Standard dar und wurde als führende Referenzanlage innerhalb der EU für die integrierte Vermeidung und Verminderung der Umweltverschmutzung als EU-Standard gelistet.</p>
  <p class="abs small" style="left:18px;top:72px;width:265px">Durch die zentrale Lage und eine mögliche Jahreskapazität von ca. 95.000 Tonnen sind wir in der Lage, die Gesamtmenge der in der Region anfallenden spezifischen Abfälle umweltgerecht zu behandeln.</p>
  <p class="abs title" style="left:18px;top:96px;font-size:11px">Eigener Fuhrpark <b>durch Tochterfirma</b></p>
  <div class="abs small" style="left:22px;top:114px;width:260px">
    <p>Mit unseren 8 Fahrzeugen decken wir eine Vielzahl von Dienstleistungen ab.</p>
    <ul style="margin:2px 0 2px 4px"><li>Kombisaugwagen</li><li>Saugwagen mit großem Fassungsvermögen</li><li>Stückguttransporter</li><li>Planen Wagen</li><li>TV-Kanalinspektionswagen</li></ul>
    <p>Nach Wunsch stellen wir Flüssigkeitsbehälter und Behälter ohne Bodenauslauf bereit.</p>
  </div>
  <div class="abs hotline" style="left:18px;top:192px">
    <div class="ic"><svg width="9" height="9" viewBox="0 0 24 24"><path d="M6 2l4 4-2 3c1 2 4 5 6 6l3-2 4 4-3 4C10 21 3 14 2 5z" fill="var(--green)"/></svg></div>
    <div><strong>24h Notdienst:</strong><span>0699/00 12 34 56</span></div>
  </div>
  <div class="abs contact" style="left:18px;top:216px"><div><i></i>www.brav.at</div><div><i></i>tankcleaning@brav.at</div></div>
  <div class="abs brand" style="left:196px;top:205px;font-size:15px"><span class="dot"></span>BRAV</div>
</section>

</body>
</html>
```